Business Card Design Project

I need a business card design for an Organic drive thru coffee kiosk. We will serve organic coffee, teas & smoothies and will serve healthy breakfast food/snacks for people on the go.
I want the card to have 2-3 colors max (earthy colors like browns, greens and so on).
I have attached the logo I want used and would love to play off the theme of "balance."
Include:
Tidy-Kettle Coffee
address: 4820 Gorvin Ct. Raleigh, NC 27583
phone: 919-731-4062
website: www.tidy-kettle.com (website is not up yet but still include it on card)
email: Rosalind@tidy-kettle.com
I want one of the following sayings somewhere on the card (the front or back is fine):
"Eat & Drink Well, on the run!"
"Break the fast with Tidy-Kettle"
Maybe on the back list what we offer:
-Organic coffee, espresso & tea
-Blendora smoothies & protein shakes
-Zesty Pour (100% fresh local fruit and veggies)
-Tender Nibs

```html
<!DOCTYPE html>
<html lang="en">
<head>
<meta charset="utf-8">
<title>Tidy-Kettle Coffee — Business Card</title>
<link rel="stylesheet" href="https://fonts.googleapis.com/css2?family=Arimo:wght@400;700&display=swap">
<style>
  :root {
    --page-bg: #e8e3dc;
    --card-bg: #3e2a21;
    --rust: #a8462d;
    --leaf: #6f9e1f;
    --leaf-soft: #5f8a1a;
  }
  * { margin: 0; padding: 0; box-sizing: border-box; }
  html, body { width: 1200px; height: 900px; overflow: hidden; }
  body {
    background: var(--page-bg);
    font-family: "Arimo", Arial, sans-serif;
    position: relative;
  }
  .card {
    position: absolute;
    left: 260px;
    width: 680px;
    height: 388px;
    background: var(--card-bg);
    border-radius: 28px;
    box-shadow: 0 6px 18px rgba(40, 25, 15, 0.25);
    overflow: hidden;
  }
  .card--back { top: 40px; }
  .card--front { top: 472px; }

  /* Brand lockup: plain dot stacked above the name */
  .brand {
    display: flex;
    flex-direction: column;
    align-items: center;
    color: var(--rust);
    font-weight: 400;
    line-height: 1;
  }
  .brand-dot {
    border-radius: 50%;
    background: var(--rust);
    flex: none;
  }

  /* Back side */
  .back-brand {
    position: absolute;
    top: 34px;
    left: 0; right: 0;
    gap: 10px;
    font-size: 48px;
  }
  .back-brand .brand-dot { width: 38px; height: 38px; }
  .accent-line {
    position: absolute;
    height: 2px;
    background: var(--leaf);
  }
  .accent-line--right { top: 112px; right: 0; width: 140px; }
  .accent-line--left { top: 292px; left: 0; width: 150px; }
  .offer-list {
    position: absolute;
    top: 160px;
    left: 0; right: 0;
    list-style: none;
    text-align: center;
    color: var(--leaf);
    font-size: 19px;
    line-height: 1.45;
  }
  .offer-list li::before { content: "• "; }
  .saying {
    position: absolute;
    top: 318px;
    left: 0; right: 0;
    text-align: center;
    color: var(--rust);
    font-size: 18px;
    letter-spacing: 0.5px;
  }

  /* Front side */
  .contact {
    position: absolute;
    top: 60px;
    left: 54px;
    color: var(--leaf);
  }
  .contact-name {
    font-size: 26px;
    font-weight: 400;
    letter-spacing: 0.5px;
  }
  .contact-role {
    font-size: 16px;
    color: var(--leaf-soft);
    margin-top: 2px;
  }
  .contact-lines {
    margin-top: 40px;
    font-size: 17px;
    line-height: 1.45;
  }
  .contact-lines .label {
    display: inline-block;
    width: 28px;
  }
  .contact-address { margin-top: 14px; font-size: 17px; }
  .contact-web { margin-top: 18px; font-size: 17px; }

  .front-brand-block {
    position: absolute;
    right: 46px;
    top: 120px;
    width: 290px;
    text-align: center;
  }
  .front-brand {
    gap: 12px;
    font-size: 50px;
  }
  .front-brand .brand-dot { width: 50px; height: 50px; }
  .front-tagline {
    margin-top: 12px;
    color: var(--rust);
    font-size: 13px;
    letter-spacing: 3.5px;
    text-transform: uppercase;
  }
</style>
</head>
<body>

<section class="card card--back" aria-label="Card back">
  <div class="brand back-brand">
    <span class="brand-dot"></span>
    <span class="brand-name">Tidy-Kettle</span>
  </div>
  <div class="accent-line accent-line--right"></div>
  <div class="accent-line accent-line--left"></div>
  <ul class="offer-list">
    <li>Organic coffee, espresso &amp; tea</li>
    <li>Blendora smoothies &amp; protein shakes</li>
    <li>Zesty Pour (100% fresh local fruit and veggies)</li>
    <li>Tender Nibs</li>
  </ul>
  <p class="saying">"Break the fast with Tidy-Kettle"</p>
</section>

<section class="card card--front" aria-label="Card front">
  <div class="contact">
    <h1 class="contact-name">ROSALIND HARTWELL</h1>
    <p class="contact-role">Operation Manager</p>
    <p class="contact-lines">
      <span class="label">T</span>919-731-4062<br>
      <span class="label">E</span>rosalind@tidy-kettle.com
    </p>
    <p class="contact-address">4820 Gorvin Ct. Raleigh, NC 27583</p>
    <p class="contact-web">www.tidy-kettle.com</p>
  </div>
  <div class="front-brand-block">
    <div class="brand front-brand">
      <span class="brand-dot"></span>
      <span class="brand-name">Tidy-Kettle</span>
    </div>
    <p class="front-tagline">Organic Coffee + Cafe</p>
  </div>
</section>

</body>
</html>
```